FoldCrest App for On-Demand Laundry

We are launching a startup of online laundry service using mobile app. This startup will give the most convenient experience for the customers in managing their laundry. In only few taps away with the app, we'll send our agents to pick up laundry at the customer's doorstep, proceed it as per their order type, and get it delivered back to them in a schedule that fits them well.

We need somebody that can help with us and make our app as one of the simplest yet most effective app to use, design should be clean and easy to navigate, leave experience that makes our users want to come back and use it again. It will consist of key features that the app should have as follows:

- Sign up & Login
- Add customer address
- Schedule laundry pick up & delivery
- Laundry service selection
- Confirmation and Payment
- Status Tracking

Please refer to the attachment for details of business flows. Example of apps that can inspire: Tidora, Rinsebox, Sudvel.

--PLEASE DO NOT USE THE LOGO FROM ATTACHMENT, IT'S ONLY A DUMMY LOGO--
Updates

Target Market(s)

Young Professional, College Students, Young Early Family

Industry/Entity Type

Cleaning Service

Font styles to use
Sans Serif

Colors
ffffff
9d9d9d
0392cd
33a6d7
86cfc6
33b8a4
acd036
cadf82

Requirements
Must have
• Simplicity and elegance. Clean and easy navigation.
• Example from attachment is "ugly" but can tell the overall idea on what information to capture from the app. We need to get a completely different design which is way better than it.
Nice to have
• Inspiration could be from similar apps like: Tidora, Rinsebox, and Sudvel.
Should not have
• --PLEASE DO NOT USE THE LOGO FROM ATTACHMENT, IT'S ONLY A DUMMY LOGO--

```html
<!DOCTYPE html>
<html lang="en">
<head>
<meta charset="utf-8">
<title>FoldCrest – UX/UI design</title>
<link rel="stylesheet" href="https://fonts.googleapis.com/css2?family=Roboto:wght@300;400;500;700&family=Tinos&display=swap">
<style>
:root{
  --navy:#34506b;
  --navy-deep:#2d475f;
  --header:#3e5d7b;
  --steps:#33506c;
  --green:#a9cd37;
  --ink:#3f4c59;
  --muted:#9aa3ab;
  --rule:#e6e9ec;
  --paper:#ffffff;
  --canvas:#ffffff;
}
*{box-sizing:border-box;margin:0;padding:0}
html,body{width:1200px;height:1200px;overflow:hidden;background:var(--canvas)}
body{position:relative;font-family:"Roboto",sans-serif;font-weight:300;color:var(--ink)}
.title{position:absolute;left:100px;top:232px}
.title h1{font-weight:300;font-size:50px;color:var(--navy);letter-spacing:.5px;line-height:1}
.title h2{font-weight:300;font-size:32px;color:var(--green);margin-top:8px;line-height:1}
.title .version{font-weight:700;font-size:32px;color:var(--navy);margin-top:42px;line-height:1}

.screen{position:absolute;overflow:hidden;background:var(--paper)}
.t{position:absolute;left:0;right:0;text-align:center;transform:translateY(-50%);white-space:nowrap}
.rule{position:absolute;left:0;right:0;height:1px;background:var(--rule)}

/* login */
.login{left:450px;top:96px;width:266px;height:472px;background:linear-gradient(180deg,#3d5b79 0%,#3a5775 60%,#34506c 100%);color:#fff}
.login .band{position:absolute;left:0;right:0;top:380px;bottom:0;background:rgba(30,50,70,.25)}
.brand{top:74px;font-size:20px;font-weight:300;display:flex;justify-content:center;align-items:center;gap:8px;transform:translateY(-50%)}
.brand i{width:12px;height:12px;border:1.5px solid #fff;display:block}
.tagline{font-size:12.5px;line-height:15px}
.field-line{position:absolute;left:46px;right:44px;height:1px;background:rgba(255,255,255,.35)}
.btn-login{position:absolute;left:46px;width:182px;top:293px;height:29px;background:var(--green);color:#fff;font-size:8px;font-weight:500;display:flex;align-items:center;justify-content:center;letter-spacing:.3px}

/* home */
.home{left:790px;top:96px;width:266px;height:472px;background:var(--navy-deep)}
.home .sky{position:absolute;left:0;right:0;top:0;height:248px;background:linear-gradient(180deg,#f7f7f7,#f0f1f1)}
.avatar{position:absolute;left:112px;top:71px;width:42px;height:42px;border-radius:50%;background:#d9c9b6}
.greet{position:absolute;left:98px;top:154px;transform:translateY(-50%);font-size:12px;color:var(--ink);white-space:nowrap;display:flex;gap:6px}
.greet .name{font-family:"Tinos",serif;color:var(--green);border-right:1px solid var(--navy);padding-right:6px}
.tile{position:absolute;width:133px;height:112px;color:#fff}
.tile.top{top:248px;background:var(--navy)}
.tile.bottom{top:360px;height:112px;border-top:1px solid rgba(0,0,0,.12)}
.tile.r{left:133px;border-left:1px solid rgba(0,0,0,.12)}
.tile svg{position:absolute;left:57px}
.tile .label{font-size:12px}
.tile .sub{font-size:9px;color:var(--green);font-weight:400}
.fab{position:absolute;left:79px;top:194px;width:108px;height:108px;border-radius:50%;background:var(--green);color:#fff;text-align:center}
.fab .plus{position:absolute;left:0;right:0;top:22px;font-size:24px;font-weight:200;color:#fff}
.fab .fab-label{position:absolute;left:0;right:0;top:56px;font-size:14px;color:#fff}

/* order flow */
.flow{top:714px;width:199px;height:355px}
.head{position:absolute;left:0;right:0;top:0;height:36px;background:var(--header);color:#fff}
.head .crumb{position:absolute;right:14px;top:18px;transform:translateY(-50%);font-size:8.5px;white-space:nowrap}
.head .crumb b{font-family:"Tinos",serif;font-weight:400;color:var(--green);font-size:9px}
.head svg{position:absolute;left:10px;top:12px}
.steps{position:absolute;left:0;right:0;top:36px;height:22px;background:var(--steps)}
.steps .track{position:absolute;left:0;top:10px;height:1px;background:var(--green)}
.dot{position:absolute;top:5px;width:12px;height:12px;margin-left:-6px;border-radius:50%;font-size:7px;color:#fff;display:flex;align-items:center;justify-content:center;font-weight:400}
.dot.on{background:var(--green);color:var(--navy)}
.lbl{font-size:8px;font-weight:400;color:var(--ink)}
.big{font-size:16px;color:#7c8791}
.small{font-size:8.5px;color:var(--muted)}
.tiny-g{font-size:6px;font-weight:500;color:var(--green);letter-spacing:.2px}
.chev{position:absolute;transform:translate(-50%,-50%)}
.btn{position:absolute;top:318px;height:22px;background:var(--header);color:#fff;font-size:6.5px;font-weight:500;display:flex;align-items:center;justify-content:center}
.total{position:absolute;left:20px;top:311px}
.total small{display:block;font-size:6px;font-weight:500;color:var(--ink)}
.total span{display:block;font-family:"Tinos",serif;font-size:18px;color:var(--green);line-height:22px}
.opt{position:absolute;width:32px;height:32px;margin-left:-16px;border-radius:50%;border:1px solid #cfd5da;display:flex;align-items:center;justify-content:center}
.opt.on{background:var(--green);border-color:var(--green)}
.cap{position:absolute;width:60px;margin-left:-30px;text-align:center;transform:translateY(-50%);white-space:nowrap}
.abs{position:absolute;transform:translate(-50%,-50%)}
</style>
</head>
<body>

<header class="title">
  <h1>FoldCrest</h1>
  <h2>UX/UI design</h2>
  <p class="version">v.2.0</p>
</header>

<!-- Login -->
<section class="screen login" role="img" aria-label="Login screen over a photo of a person carrying laundry">
  <div class="band"></div>
  <div class="t brand"><i></i>FoldCrest</div>
  <p class="t tagline" style="top:137px">Leave the laundry to us,<br>you go out and have some fun!</p>
  <p class="t" style="top:215px;font-size:12px">Username</p>
  <div class="field-line" style="top:229px"></div>
  <p class="t" style="top:259px;font-size:12px;letter-spacing:1px;font-weight:700">●●●●●●●</p>
  <div class="field-line" style="top:269px"></div>
  <div class="btn-login">LOG IN</div>
  <p class="t" style="top:342px;font-size:12px">Forgot your password?</p>
  <p class="t" style="top:433px;font-size:12px">First time? Register</p>
</section>

<!-- Home -->
<section class="screen home">
  <div class="sky" role="img" aria-label="Light line illustration of a city skyline with clouds and sun"></div>
  <svg class="abs" style="left:133px;top:31px" width="12" height="12" viewBox="0 0 12 12"><path d="M1 1L11 11M11 1L1 11" stroke="#3f4c59" stroke-width="1"/></svg>
  <div class="avatar" role="img" aria-label="User profile photo"></div>
  <p class="greet"><span class="name">Mira</span><span>Any laundry to do?</span></p>
  <svg style="position:absolute;left:190px;top:166px" width="30" height="50" viewBox="0 0 30 50"><path d="M16 2C28 16 22 34 4 44" fill="none" stroke="#a9cd37" stroke-width="1" stroke-dasharray="3 2"/><path d="M4 38L3 45L10 44" fill="none" stroke="#a9cd37" stroke-width="1"/></svg>
  <div class="tile top">
    <svg style="top:38px" width="18" height="18" viewBox="0 0 18 18"><rect x="3.5" y="2.5" width="11" height="14" fill="none" stroke="#fff"/><path d="M6 1.5h6v2H6zM6 7h6M6 10h6M6 13h6" fill="none" stroke="#fff"/></svg>
    <p class="t label" style="top:69px">My orders</p>
    <p class="t sub" style="top:86px">Last order: delivery</p>
  </div>
  <div class="tile top r">
    <svg style="top:38px;left:56px" width="20" height="18" viewBox="0 0 20 18"><rect x="2.5" y="4.5" width="15" height="11" fill="none" stroke="#fff"/><path d="M4 4.5L14 1.5V4.5M11 8.5h6.5v3H11z" fill="none" stroke="#fff"/></svg>
    <p class="t label" style="top:69px">Wallet</p>
    <p class="t sub" style="top:86px">+ $12.25</p>
  </div>
  <div class="tile bottom">
    <svg style="top:41px" width="18" height="18" viewBox="0 0 18 18"><circle cx="9" cy="9" r="7.5" fill="none" stroke="#fff"/><text x="9" y="12" text-anchor="middle" font-size="8" fill="#fff" font-family="Roboto">$</text></svg>
    <p class="t label" style="top:73px">Pricing</p>
  </div>
  <div class="tile bottom r">
    <svg style="top:41px" width="18" height="18" viewBox="0 0 18 18"><circle cx="9" cy="9" r="3" fill="none" stroke="#fff"/><path d="M9 1.5l1.5 2.3 2.6-.9.4 2.7 2.7.4-.9 2.6 2.2 1.4-2.2 1.4.9 2.6-2.7.4-.4 2.7-2.6-.9L9 16.5l-1.5-2.3-2.6.9-.4-2.7-2.7-.4.9-2.6L1.5 9l2.2-1.4-.9-2.6 2.7-.4.4-2.7 2.6.9z" fill="none" stroke="#fff" stroke-width=".9"/></svg>
    <p class="t label" style="top:73px">Settings</p>
  </div>
  <div class="fab"><span class="plus">+</span><span class="fab-label">New order</span></div>
</section>

<!-- Step 1: Pickup -->
<section class="screen flow" style="left:89px">
  <div class="head">
    <svg width="12" height="12" viewBox="0 0 12 12"><path d="M2 2L10 10M10 2L2 10" stroke="#fff"/></svg>
    <p class="crumb"><b>New order</b> | Pickup</p>
  </div>
  <div class="steps"><div class="track" style="width:28px"></div>
    <span class="dot on" style="left:28px">1</span><span class="dot" style="left:75px">2</span><span class="dot" style="left:124px">3</span><span class="dot" style="left:172px">4</span></div>
  <p class="t lbl" style="top:72px">Address</p>
  <div class="rule" style="top:82px"></div>
  <p class="t small" style="top:104px;line-height:11px;left:-12px">412 Alder Lane<br>Maple Ridge, WA 98012</p>
  <svg class="chev" style="left:24px;top:104px" width="8" height="5" viewBox="0 0 8 5"><path d="M1 1l3 3 3-3" fill="none" stroke="#a9cd37"/></svg>
  <svg class="abs" style="left:187px;top:103px" width="17" height="17" viewBox="0 0 17 17"><circle cx="8.5" cy="8.5" r="7.5" fill="none" stroke="#a9cd37"/><path d="M8.5 4.5v8M4.5 8.5h8" stroke="#a9cd37"/></svg>
  <div class="rule" style="top:130px"></div>
  <p class="t lbl" style="top:139px">Date</p>
  <div class="rule" style="top:148px"></div>
  <p class="t tiny-g" style="top:161px;left:134px;right:auto">SAT</p>
  <p class="t big" style="top:174px">12. Mar 2016</p>
  <svg class="chev" style="left:28px;top:174px" width="5" height="8" viewBox="0 0 5 8"><path d="M4 1L1 4l3 3" fill="none" stroke="#a9cd37"/></svg>
  <svg class="chev" style="left:173px;top:174px" width="5" height="8" viewBox="0 0 5 8"><path d="M1 1l3 3-3 3" fill="none" stroke="#a9cd37"/></svg>
  <div class="rule" style="top:194px"></div>
  <p class="t lbl" style="top:203px">Time</p>
  <div class="rule" style="top:212px"></div>
  <svg class="chev" style="left:68px;top:224px" width="8" height="5" viewBox="0 0 8 5"><path d="M1 4l3-3 3 3" fill="none" stroke="#a9cd37"/></svg>
  <svg class="chev" style="left:131px;top:224px" width="8" height="5" viewBox="0 0 8 5"><path d="M1 4l3-3 3 3" fill="none" stroke="#a9cd37"/></svg>
  <p class="t big" style="top:239px">11:00 to 12:00 <span class="tiny-g" style="vertical-align:4px">AM</span></p>
  <svg class="chev" style="left:68px;top:256px" width="8" height="5" viewBox="0 0 8 5"><path d="M1 1l3 3 3-3" fill="none" stroke="#a9cd37"/></svg>
  <svg class="chev" style="left:131px;top:256px" width="8" height="5" viewBox="0 0 8 5"><path d="M1 1l3 3 3-3" fill="none" stroke="#a9cd37"/></svg>
  <div class="rule" style="top:267px"></div>
  <p class="t" style="top:290px;font-size:8.5px;color:var(--green)"><svg width="14" height="14" viewBox="0 0 14 14" style="vertical-align:-4px;margin-right:3px"><circle cx="7" cy="7" r="6.3" fill="none" stroke="#a9cd37"/><path d="M4.5 9.5l.5-2 3.5-3.5 1.5 1.5L6.5 9z" fill="none" stroke="#a9cd37" stroke-width=".8"/></svg>Add notes</p>
  <div class="btn" style="left:59px;width:81px">NEXT</div>
</section>

<!-- Step 2: Service -->
<section class="screen flow" style="left:346px">
  <div class="head">
    <svg width="12" height="12" viewBox="0 0 12 12"><path d="M8 2L4 6L8 10" fill="none" stroke="#fff"/></svg>
    <p class="crumb"><b>New order</b> | Service</p>
  </div>
  <div class="steps"><div class="track" style="width:75px"></div>
    <span class="dot on" style="left:28px">1</span><span class="dot on" style="left:75px">2</span><span class="dot" style="left:124px">3</span><span class="dot" style="left:172px">4</span></div>
  <p class="t lbl" style="top:72px">Service speed</p>
  <div class="rule" style="top:82px"></div>
  <div class="opt" style="left:44px;top:93px"><svg width="12" height="14" viewBox="0 0 12 14"><circle cx="6" cy="3" r="1.8" fill="none" stroke="#a9cd37"/><path d="M4 6h4v4H7v3H5v-3H4z" fill="none" stroke="#a9cd37"/></svg></div>
  <div class="opt on" style="left:100px;top:93px"><svg width="16" height="10" viewBox="0 0 16 10"><path d="M1 7V5l3-3h6l3 3h2v2z" fill="none" stroke="#fff"/><circle cx="4.5" cy="8" r="1.2" fill="#fff"/><circle cx="11.5" cy="8" r="1.2" fill="#fff"/></svg></div>
  <div class="opt" style="left:155px;top:93px"><svg width="10" height="14" viewBox="0 0 10 14"><path d="M5 1C7 3 7 7 7 10H3C3 7 3 3 5 1zM3 10L1.5 12.5M7 10l1.5 2.5" fill="none" stroke="#a9cd37"/></svg></div>
  <p class="cap small" style="left:44px;top:134px">Regular</p><p class="cap tiny-g" style="left:44px;top:143px">4 DAYS</p>
  <p class="cap small" style="left:100px;top:134px">Express</p><p class="cap tiny-g" style="left:100px;top:143px">2 DAYS</p>
  <p class="cap small" style="left:155px;top:134px">Cosmic</p><p class="cap tiny-g" style="left:155px;top:143px">1 DAY</p>
  <div class="rule" style="top:155px"></div>
  <p class="t lbl" style="top:164px">Service list</p>
  <div class="rule" style="top:174px"></div>
  <div class="opt on" style="left:44px;top:182px"><svg width="14" height="12" viewBox="0 0 14 12"><path d="M7 1v10M2 3h10M2 3L0.5 7h3zM12 3l-1.5 4h3zM4 11h6" fill="none" stroke="#fff" stroke-width=".8"/></svg></div>
  <div class="opt on" style="left:100px;top:182px"><svg width="16" height="10" viewBox="0 0 16 10"><path d="M8 1.5a1.5 1.5 0 1 1 0 2.5v1.5L1 9h14L8 5.5" fill="none" stroke="#fff" stroke-width=".9"/></svg></div>
  <div class="opt" style="left:155px;top:182px"><svg width="12" height="13" viewBox="0 0 12 13"><rect x="1.5" y="1.5" width="9" height="10" fill="none" stroke="#a9cd37"/><circle cx="6" cy="7" r="2.3" fill="none" stroke="#a9cd37"/></svg></div>
  <p class="cap small" style="left:44px;top:222px">Kg Wash</p>
  <p class="cap small" style="left:100px;top:222px">Pc Wash</p>
  <p class="cap small" style="left:155px;top:222px">Dry Clean</p>
  <p class="cap big" style="left:44px;top:242px;font-size:15px"><span style="color:var(--green);font-size:9px">−&nbsp;&nbsp;</span> 4 <span style="color:var(--green);font-size:9px">&nbsp;&nbsp;+</span></p>
  <p class="cap big" style="left:100px;top:242px;font-size:15px"><span style="color:var(--green);font-size:9px">−&nbsp;&nbsp;</span> 2 <span style="color:var(--green);font-size:9px">&nbsp;&nbsp;+</span></p>
  <p class="cap big" style="left:155px;top:242px;font-size:15px;color:#dfe3e6"><span style="font-size:9px">−&nbsp;&nbsp;</span> 0 <span style="font-size:9px">&nbsp;&nbsp;+</span></p>
  <p class="cap tiny-g" style="left:44px;top:258px">KG</p><p class="cap tiny-g" style="left:100px;top:258px">PC</p><p class="cap" style="left:155px;top:258px;font-size:6px;color:#d5d9dc">KG</p>
  <div class="rule" style="top:266px"></div>
  <p class="cap" style="left:44px;top:280px;font-family:Tinos,serif;font-size:10.5px;color:var(--green)">$10.00</p>
  <p class="cap" style="left:100px;top:280px;font-family:Tinos,serif;font-size:10.5px;color:var(--green)">$2.00</p>
  <p class="cap" style="left:155px;top:280px;font-size:8px;color:#d5d9dc">-</p>
  <div class="rule" style="top:294px"></div>
  <div class="total"><small>TOTAL CHARGED</small><span>$12.00</span></div>
  <div class="btn" style="left:100px;width:80px">NEXT</div>
</section>

<!-- Step 3: Return -->
<section class="screen flow" style="left:603px">
  <div class="head">
    <svg width="12" height="12" viewBox="0 0 12 12"><path d="M8 2L4 6L8 10" fill="none" stroke="#fff"/></svg>
    <p class="crumb"><b>New order</b> | Return</p>
  </div>
  <div class="steps"><div class="track" style="width:124px"></div>
    <span class="dot on" style="left:28px">1</span><span class="dot on" style="left:75px">2</span><span class="dot on" style="left:124px">3</span><span class="dot" style="left:172px">4</span></div>
  <p class="t lbl" style="top:72px">Return date</p>
  <div class="rule" style="top:82px"></div>
  <p class="t tiny-g" style="top:96px;left:138px;right:auto">MON</p>
  <p class="t big" style="top:110px">14. Mar 2016</p>
  <svg class="chev" style="left:160px;top:110px" width="5" height="8" viewBox="0 0 5 8"><path d="M1 1l3 3-3 3" fill="none" stroke="#a9cd37"/></svg>
  <div class="rule" style="top:132px"></div>
  <p class="t lbl" style="top:143px">Return date</p>
  <div class="rule" style="top:154px"></div>
  <svg class="chev" style="left:68px;top:168px" width="8" height="5" viewBox="0 0 8 5"><path d="M1 4l3-3 3 3" fill="none" stroke="#a9cd37"/></svg>
  <svg class="chev" style="left:131px;top:168px" width="8" height="5" viewBox="0 0 8 5"><path d="M1 4l3-3 3 3" fill="none" stroke="#a9cd37"/></svg>
  <p class="t big" style="top:184px">11:00 to 12:00 <span class="tiny-g" style="vertical-align:4px">AM</span></p>
  <svg class="chev" style="left:68px;top:201px" width="8" height="5" viewBox="0 0 8 5"><path d="M1 1l3 3 3-3" fill="none" stroke="#a9cd37"/></svg>
  <svg class="chev" style="left:131px;top:201px" width="8" height="5" viewBox="0 0 8 5"><path d="M1 1l3 3 3-3" fill="none" stroke="#a9cd37"/></svg>
  <div class="rule" style="top:215px"></div>
  <div class="total"><small>TOTAL CHARGED</small><span>$12.00</span></div>
  <div class="btn" style="left:100px;width:80px">NEXT</div>
</section>

<!-- Step 4: Summary -->
<section class="screen flow" style="left:860px">
  <div class="head">
    <svg width="12" height="12" viewBox="0 0 12 12"><path d="M8 2L4 6L8 10" fill="none" stroke="#fff"/></svg>
    <p class="crumb"><b>New order</b> | Summary</p>
  </div>
  <div class="steps"><div class="track" style="width:172px"></div>
    <span class="dot on" style="left:28px">1</span><span class="dot on" style="left:75px">2</span><span class="dot on" style="left:124px">3</span><span class="dot on" style="left:172px">4</span></div>
  <p class="t lbl" style="top:72px">Order #12446</p>
  <div class="rule" style="top:82px"></div>
  <p class="t tiny-g" style="top:95px">11:00 TO 12:00</p>
  <p class="t big" style="top:108px">12. Mar 2016</p>
  <div class="rule" style="top:126px"></div>
  <p class="t small" style="top:147px;line-height:11px">412 Alder Lane<br>Maple Ridge, WA 98012</p>
  <div class="rule" style="top:168px"></div>
  <p class="t tiny-g" style="top:182px">EXPRESS SERVICE - 2 DAYS</p>
  <div class="rule" style="top:198px"></div>
  <p class="small" style="position:absolute;left:42px;top:209px;line-height:11px">4 Kg(s) Wash<br>3 Pc(s) Wash</p>
  <p style="position:absolute;right:48px;top:209px;line-height:11px;text-align:right;font-family:Tinos,serif;font-size:9.5px;color:var(--green)">$10.00<br>$2.00</p>
  <div class="rule" style="top:245px"></div>
  <p class="t tiny-g" style="top:258px">11:00 TO 12:00</p>
  <p class="t big" style="top:271px">14. Mar 2016</p>
  <div class="rule" style="top:290px"></div>
  <div class="total"><small>TOTAL CHARGED</small><span>$12.00</span></div>
  <div class="btn" style="left:100px;width:80px">CONFIRM</div>
</section>

</body>
</html>
```